Democracy in crisis book

This book tries to sound the ALARM that we will lose our democracy unless we force Unionists to adopt the plan inside this book. I designed a mock cover (attached) but I am concerned it would not look good in the Thumbnail view that most people would see it as they're scrolling down Shopvale or Pagenook. The final title for the book is: Final Hour to Rescue the Free Republic. The current subtitle is: The Single Path to Halt the 2022 Partisan Takeover & Renew Our Homeland -- but it’s a work in progress.The subtitle is still working progress but it's really not that important and can be small.
STYLE CONSIDERATIONS:
(1) The title should be on 5 separate lines: Final; Hour; To Rescue; Free; Republic
(2) The title could be in white fat letters except for maybe one line that says “To Rescue” which could be in the blue color of the Civic Union Party-- or maybe Free Republic could be in blue. We may have to try a few variations of that.
(3) I picked the red in the mock cover to connotate an emergency,
(4) I liked big bold fat font going across the full page so that it looks like a major warning sign, though note I was unable to extend each line flush all the way to the right which I think would have been better.
(5) I liked it better flush to left instead of centered.
(6) I picked the Harwick monument + a crowd for my mock cover, but a picture of a huge crowd protesting with a picture of the United States Congress in the background would be much better. DO NOT USE HARWICK. Obviously I would need it to be an open license or something I can pay a small amount to get. If you can find that picture then the page should probably be colored in red with Congress in white.
I got the idea 4 giant title from the book “seldom a quiet so bright” and Dellowby’s “When Freedom Fades” or “Grey Herons” by Mara Vostell though I hate that font)
I love Osric Thale’s “marked since the outset” cover so if you find a picture of Congress and a protest crowd instead of painting it red you could have just a couple of jagged red stripes going across it like that cover.
I love the 3-D effect of Greta Wolven's cover for The Silverwren where it looks like a page is being ripped. That effect could be done the words Free Republic like it's being torn off the page UPDATE: MANY DESIGNERS TRIED THAT & IT DID NOT WORK AT ALL.
Note that this book will be submitted to many award competitions, so please give me an award-winning cover.
I like how the title of the book The Unchosen by Martin Fellowes has the words starting to fade. I don't like the ladder on it, but maybe 'Free Republic' could fade like that.
Unionists

```html
<!DOCTYPE html>
<html lang="en">
<head>
<meta charset="utf-8">
<title>Final Hour to Rescue the Free Republic — Book Cover</title>
<link rel="stylesheet" href="https://fonts.googleapis.com/css2?family=Bebas+Neue&family=Oswald:wght@400;500&display=swap">
<style>
  :root {
    --stage: #e4e5e6;
    --alarm-red: #a30f1b;
    --alarm-red-deep: #5c060d;
    --alarm-red-mid: #7e0a14;
    --title-white: #f4ecec;
    --text-white: #f6eeee;
  }
  * { box-sizing: border-box; margin: 0; padding: 0; }
  html, body {
    width: 1200px;
    height: 900px;
    overflow: hidden;
    background: var(--stage);
  }
  .book-cover {
    position: absolute;
    left: 340px;
    top: 40px;
    width: 520px;
    height: 820px;
    overflow: hidden;
    background: var(--alarm-red);
  }
  .cover-photo {
    position: absolute;
    inset: 0;
    background:
      linear-gradient(180deg,
        var(--alarm-red) 0%,
        var(--alarm-red-mid) 28%,
        var(--alarm-red) 45%,
        var(--alarm-red-mid) 62%,
        var(--alarm-red-deep) 100%);
  }
  .title {
    position: absolute;
    left: 42px;
    top: 58px;
    font-family: "Bebas Neue", "Oswald", sans-serif;
    font-weight: 400;
    color: var(--title-white);
    text-transform: uppercase;
    line-height: 0.8;
    letter-spacing: 0.005em;
    white-space: nowrap;
  }
  .title-line { display: block; }
  .title-line--final   { font-size: 212px; }
  .title-line--hour    { font-size: 176px; }
  .title-line--rescue  { font-size: 112px; }
  .title-line--free    { font-size: 120px; }
  .title-line--republic {
    font-size: 120px;
    background: linear-gradient(180deg,
      rgba(244,236,236,0.15) 0%,
      rgba(244,236,236,0.55) 35%,
      var(--title-white) 70%);
    -webkit-background-clip: text;
    background-clip: text;
    color: transparent;
  }
  .subtitle {
    position: absolute;
    left: 140px;
    width: 240px;
    top: 672px;
    font-family: "Oswald", sans-serif;
    font-weight: 400;
    font-size: 14px;
    line-height: 1.3;
    text-align: center;
    color: var(--text-white);
  }
  .author {
    position: absolute;
    left: 30px;
    right: 30px;
    top: 748px;
    font-family: "Oswald", sans-serif;
    font-weight: 500;
    font-size: 20px;
    letter-spacing: 0.06em;
    text-align: center;
    color: var(--text-white);
    text-transform: uppercase;
  }
</style>
</head>
<body>
  <main class="book-cover">
    <div class="cover-photo" role="img" aria-label="Photograph of the United States Capitol dome with a large protesting crowd in the foreground, tinted deep red"></div>
    <h1 class="title">
      <span class="title-line title-line--final">Final</span>
      <span class="title-line title-line--hour">Hour</span>
      <span class="title-line title-line--rescue">To Rescue</span>
      <span class="title-line title-line--free">Free</span>
      <span class="title-line title-line--republic">Republic</span>
    </h1>
    <p class="subtitle">The Single Path to Halt the 2022 Partisan Takeover &amp; Renew Our Homeland</p>
    <p class="author">By Rowan Ellis Tamsworth</p>
  </main>
</body>
</html>
```